Painting Contractor Business Card Design

We are looking for a cool, bold, modern, polished, business card design. We are a high-end residential painting contractor. Please incorporate our logo and keep with our green/black color scheme. We are interested in seeing 2-sided and 1-sided options. Thank you very much!

Industry/Entity Type

Business

Contact Information for Business Card

Info for the card:
Dale Ormsby
mobile 206-555-0193
email dale@tallowbrookpainting.net
web www.tallowbrookpainting.net

```html
<!DOCTYPE html>
<html lang="en">
<head>
<meta charset="UTF-8">
<title>Tallowbrook Painting – Business Card</title>
<link rel="stylesheet" href="https://fonts.googleapis.com/css2?family=Lato:wght@400;700;900&display=swap">
<style>
  :root {
    --stage: #e9e7e3;
    --card-white: #ffffff;
    --card-black: #0c0c0c;
    --ink: #2b2b2b;
    --ink-soft: #4a4a4a;
    --green: #4cb35a;
    --white: #ffffff;
  }
  * { margin: 0; padding: 0; box-sizing: border-box; }
  html, body {
    width: 1200px;
    height: 1023px;
    overflow: hidden;
    background: var(--stage);
    font-family: "Lato", Arial, sans-serif;
  }
  .stage {
    position: relative;
    width: 1200px;
    height: 1023px;
  }
  .card {
    position: absolute;
    left: 200px;
    width: 800px;
    height: 457px;
    border-radius: 26px;
    box-shadow: 0 10px 30px rgba(0,0,0,0.18);
    overflow: hidden;
  }
  .card--front {
    top: 36px;
    background: var(--card-white);
  }
  .card--back {
    top: 529px;
    background: linear-gradient(160deg, #262626 0%, var(--card-black) 55%, #050505 100%);
    display: flex;
    align-items: center;
    justify-content: center;
  }
  .brand {
    display: flex;
    align-items: center;
    gap: 14px;
  }
  .brand__mark {
    width: 30px;
    height: 30px;
    background: var(--green);
  }
  .brand__name {
    font-weight: 900;
    letter-spacing: 1px;
    text-transform: uppercase;
  }
  .card--front .brand {
    position: absolute;
    left: 62px;
    top: 150px;
  }
  .card--front .brand__name {
    font-size: 38px;
    color: var(--ink);
  }
  .card--back .brand__mark {
    width: 44px;
    height: 44px;
  }
  .card--back .brand__name {
    font-size: 54px;
    color: var(--white);
  }
  .holder {
    position: absolute;
    left: 62px;
    top: 238px;
    font-size: 26px;
    font-weight: 900;
    color: var(--ink);
  }
  .contact-list {
    position: absolute;
    left: 132px;
    top: 290px;
    list-style: none;
  }
  .contact-list li {
    display: flex;
    align-items: center;
    gap: 12px;
    font-size: 21px;
    color: var(--ink-soft);
    line-height: 36px;
  }
  .contact-list svg {
    width: 18px;
    height: 18px;
    flex: none;
  }
</style>
</head>
<body>
<main class="stage">
  <section class="card card--front" aria-label="Business card front">
    <div class="brand">
      <span class="brand__mark"></span>
      <span class="brand__name">Tallowbrook Painting</span>
    </div>
    <p class="holder">Dale Ormsby</p>
    <ul class="contact-list">
      <li>
        <svg viewBox="0 0 18 18" aria-hidden="true"><rect x="3" y="1" width="12" height="16" rx="2" fill="none" stroke="var(--green)" stroke-width="2"/><circle cx="9" cy="14" r="1.2" fill="var(--green)"/></svg>
        206-555-0193
      </li>
      <li>
        <svg viewBox="0 0 18 18" aria-hidden="true"><rect x="1" y="3" width="16" height="12" rx="1.5" fill="var(--green)"/><path d="M2 4 L9 10 L16 4" fill="none" stroke="#fff" stroke-width="1.6"/></svg>
        dale@tallowbrookpainting.net
      </li>
      <li>
        <svg viewBox="0 0 18 18" aria-hidden="true"><circle cx="9" cy="9" r="8" fill="var(--green)"/><path d="M1 9 H17 M9 1 C5 5 5 13 9 17 M9 1 C13 5 13 13 9 17" fill="none" stroke="#fff" stroke-width="1.2"/></svg>
        www.tallowbrookpainting.net
      </li>
    </ul>
  </section>

  <section class="card card--back" aria-label="Business card back">
    <div class="brand">
      <span class="brand__mark"></span>
      <span class="brand__name">Tallowbrook Painting</span>
    </div>
  </section>
</main>
</body>
</html>
```